Redesign of General Contractor Website

I currently have a wordpress site that needs some work. I would like to revitalize what we currently have to look more modern and up-to-date.
I want to be able to easily post pictures from new jobs and have a link to my own blog (not yet online). My current website can be found at www.brakvanbuilders.com
the attached pictures are a site I built in Muse. i really like that sort of theme.
PLEASE NOTE: I am not interested in completely remaking the site, simply adding more functionalty and spicing it up a bit. (more animation, interactive elements, layering, etc...)
Target Market(s)
Property owners, Home owners, business owners, property managers, Decision makers purchasing a construction project, specifically Remodels, renovations, or damage restoration, with some or limited knowledge about how to complete one of those projects.
Industry/Entity Type
Contractor
Coding
Coded - Design and coding required
Number of Pages Required
1 page
Requirements
Must have
- Updateable photo bank displaying pictures from recent jobs that we can easily change and update. An embedded youtube pane showing our most recent video via our youtube channel. Animation and/or transition effects. The small circular logos must stay (I would like to see these be used with animation/transitional effects.
- Must be consistent with other marketing material. This can be found on our facebook page or in the power point file attached.
- Must use colors and fonts found at www.brakvanbuilders.com
Nice to have
- Stock photos available if needed.
Should not have
- changes in logo design or re wording of text (use lorim ipsum if needed)
- No multiple pages, redesigning fonts

```html
<!DOCTYPE html>
<html lang="en">
<head>
<meta charset="utf-8">
<title>Brakvan Builders</title>
<link rel="stylesheet" href="https://fonts.googleapis.com/css2?family=Montserrat:ital,wght@0,400;0,600;0,700;1,500&family=Open+Sans:wght@400;600&display=swap">
<style>
:root{
  --orange:#f26a21;
  --orange-dark:#d95510;
  --navy:#2b3f8c;
  --navy-deep:#1f2f6e;
  --ink:#3a3a3a;
  --muted:#777;
  --grey-band:#ececec;
  --white:#ffffff;
}
*{box-sizing:border-box;margin:0;padding:0}
html,body{width:1200px;height:4401px;overflow:hidden}
body{position:relative;background:var(--white);font-family:"Open Sans",Arial,sans-serif;color:var(--ink)}
.section{position:absolute;left:0;width:1200px}
.heading{font-family:"Montserrat",Arial,sans-serif;font-weight:700;font-size:46px;color:var(--navy);text-align:center;letter-spacing:.5px}
.heading .accent{color:var(--orange)}
.heading-mark{display:block;width:22px;height:22px;background:var(--orange);margin:0 auto 14px}
.btn{display:inline-block;font-family:"Montserrat",Arial,sans-serif;font-weight:700;font-size:19px;color:var(--white);background:var(--navy);padding:16px 32px;border-radius:30px 4px 30px 4px;letter-spacing:.5px}
.body-copy{font-size:14px;line-height:1.75;color:var(--muted)}

/* top bar */
.top-bar{top:0;height:44px;background:var(--orange);color:var(--white);font-size:13px;display:flex;justify-content:space-between;align-items:center;padding:0 40px}
.top-bar span{display:flex;align-items:center;gap:10px}

/* hero */
.hero{top:44px;height:581px;background:linear-gradient(100deg,#c9a35a 0%,#9eb0c4 28%,#7f97b3 55%,#5f7796 100%)}
.nav{position:absolute;top:14px;left:90px;width:1020px;height:100px;display:flex;align-items:center;justify-content:space-between;font-family:"Montserrat",Arial,sans-serif;font-weight:600;font-size:16px;color:var(--navy)}
.nav-pill{background:rgba(255,255,255,.9);height:64px;display:flex;align-items:center;gap:48px;padding:0 40px;border-radius:6px}
.nav-pill .active{background:var(--navy);color:var(--white);padding:14px 34px;border-radius:24px 4px 24px 4px;margin-left:-30px}
.brand{display:flex;align-items:center;gap:10px;background:var(--white);padding:16px 22px;border-radius:6px;font-family:"Montserrat",Arial,sans-serif;font-weight:700;font-size:30px;color:var(--navy)}
.brand i{display:block;width:20px;height:20px;background:var(--orange)}
.hero-text{position:absolute;right:50px;top:155px;width:560px;text-align:right;color:var(--white)}
.hero-text h1{font-family:"Montserrat",Arial,sans-serif;font-weight:700;font-size:56px;letter-spacing:1px;line-height:1.15}
.hero-text p{font-size:15px;line-height:1.7;margin:12px 0 26px}
.hero-text .btn{background:var(--navy);font-size:20px}
.hero-arrow{position:absolute;top:300px}

/* mission */
.mission{top:625px;height:293px;background:var(--navy)}
.mission-tag{position:absolute;left:0;top:0;width:337px;height:293px;background:var(--orange);display:flex;flex-direction:column;align-items:center;justify-content:center}
.mission-tag .heading-mark{background:var(--navy)}
.mission-tag .heading{color:var(--navy);line-height:1.05;font-size:44px}
.mission-copy{position:absolute;left:378px;top:38px;width:780px;color:#dfe4f5;font-size:13.5px;line-height:1.7}
.mission-copy p{margin-bottom:10px}
.mission-copy .rating{color:var(--orange)}

/* work */
.work{top:918px;height:462px}
.work-text{position:absolute;left:80px;top:40px;width:440px}
.work-text .heading{text-align:left}
.work-text .heading-mark{margin:0 0 14px}
.work-text p{margin-top:18px}
.work-text .btn{margin-top:26px}
.video{position:absolute;left:601px;top:109px;width:523px;height:300px;background:#111}
.video-frame{position:absolute;left:0;top:0;width:523px;height:300px;background:linear-gradient(135deg,#5a5a5a,#2a2a2a 60%,#444)}
.video-url{position:absolute;left:12px;top:8px;color:var(--white);font-size:13px}
.video-badge{position:absolute;left:186px;top:75px;width:150px;height:150px;border-radius:50%;background:var(--white);display:flex;align-items:center;justify-content:center;font-family:"Montserrat",Arial,sans-serif;font-weight:700;font-size:22px;color:var(--navy)}
.video-bar{position:absolute;left:0;bottom:0;width:523px;height:30px;background:rgba(0,0,0,.85);display:flex;align-items:center;padding:0 12px;gap:12px;color:#ddd;font-size:11px}
.video-bar .track{flex:1;height:3px;background:#555}

/* services */
.services{top:1380px;height:727px;background:var(--grey-band)}
.services-intro{width:720px;margin:18px auto 0;text-align:center}
.service-row{position:absolute;top:240px;left:75px;width:1050px;display:flex;justify-content:space-between}
.service{width:92px;text-align:center;font-family:"Montserrat",Arial,sans-serif;font-weight:600;font-size:14px;color:var(--orange)}
.service .dot{width:80px;height:80px;border-radius:50%;background:var(--orange);margin:0 auto 12px;display:flex;align-items:center;justify-content:center}
.service.current .dot{background:var(--navy)}
.service.current span{color:var(--navy);border-bottom:3px solid var(--navy);padding-bottom:4px}
.service-panel{position:absolute;left:79px;top:404px;width:1041px;height:261px;background:var(--navy);border-radius:6px;color:var(--white)}
.service-panel .art{position:absolute;left:0;top:40px;width:285px;height:150px;background:linear-gradient(160deg,#4a4a4a,#1e1e1e)}
.service-panel h3{position:absolute;left:340px;top:32px;font-family:"Montserrat",Arial,sans-serif;font-weight:700;font-size:36px}
.service-panel p{position:absolute;left:340px;top:92px;width:650px;font-size:13.5px;line-height:1.75;color:#dfe4f5}
.panel-notch{position:absolute;left:100px;top:-14px;width:0;height:0;border-left:14px solid transparent;border-right:14px solid transparent;border-bottom:14px solid var(--navy)}

/* painting */
.painting{top:2107px;height:298px;background:var(--navy)}
.paint-brands{position:absolute;left:0;top:0;width:332px;height:298px;background:var(--orange);display:flex;flex-direction:column;justify-content:center;gap:26px;padding-left:90px;font-family:"Montserrat",Arial,sans-serif;font-weight:700;color:var(--navy)}
.paint-brands .b1{font-size:30px}
.paint-brands .b2{font-size:16px}
.paint-brands .b3{font-size:24px}
.paint-copy{position:absolute;left:332px;top:0;width:868px;text-align:center;color:var(--white)}
.paint-copy h2{margin-top:42px;font-family:"Montserrat",Arial,sans-serif;font-weight:700;font-size:32px;line-height:1.35}
.paint-copy h2 .accent{color:var(--orange)}
.paint-copy .sub{font-family:"Montserrat",Arial,sans-serif;font-style:italic;font-weight:500;font-size:16px;color:#c7cfee;margin-top:8px}
.call{margin-top:32px;display:flex;justify-content:center;align-items:center;gap:18px;font-family:"Montserrat",Arial,sans-serif;font-weight:600;font-size:34px}
.call .ring{width:60px;height:60px;border-radius:50%;background:var(--orange);display:flex;align-items:center;justify-content:center}

/* about */
.about{top:2405px;height:485px}
.about-copy{width:1000px;margin:22px auto 0;text-align:center}
.about-copy p{margin-bottom:14px}
.about .btn{position:absolute;left:513px;top:380px}

/* team */
.team{top:2890px;height:485px;background:var(--grey-band)}
.member{position:absolute;top:210px;width:520px}
.member .portrait{position:absolute;left:0;top:0;width:190px;height:210px;clip-path:polygon(50% 0,100% 25%,100% 75%,50% 100%,0 75%,0 25%);background:linear-gradient(160deg,#d6d3cf,#8c8580)}
.member .info{position:absolute;left:220px;top:2px;width:300px}
.member h4{font-family:"Montserrat",Arial,sans-serif;font-weight:700;font-size:19px;color:var(--orange)}
.member .role{font-style:italic;font-size:13px;color:var(--navy);text-decoration:underline;margin:4px 0 14px}
.member p{font-size:13px;line-height:1.7;color:var(--muted)}

/* contact */
.contact{top:3375px;height:527px;background:var(--orange)}
.contact .heading{color:var(--navy)}
.contact .heading .accent{color:var(--white)}
.form-title{position:absolute;top:170px;left:80px;width:700px;text-align:center;font-family:"Montserrat",Arial,sans-serif;font-weight:700;font-size:16px;color:var(--navy)}
.field{position:absolute;background:rgba(255,255,255,.92);border:1px solid #e3b79b;font-size:12px;color:#999;padding:12px}
.send{position:absolute;left:132px;top:360px;width:100px;height:100px;border-radius:50%;background:var(--navy);border:8px solid #1b2a66;display:flex;align-items:center;justify-content:center}
.info-title{position:absolute;top:170px;left:850px;width:250px;text-align:center;font-family:"Montserrat",Arial,sans-serif;font-weight:700;font-size:16px;color:var(--navy)}
.info-map{position:absolute;left:855px;top:200px;width:190px;height:190px;border-radius:50%;background:radial-gradient(circle at 40% 40%,#3c5bb0,#22377a)}
.info-card{position:absolute;left:893px;top:295px;width:225px;height:160px;background:var(--navy);color:var(--white);font-size:12.5px;text-align:center;padding:14px 10px 0}
.info-card strong{font-family:"Montserrat",Arial,sans-serif;font-size:15px;display:block}
.info-line{display:flex;align-items:center;gap:10px;justify-content:center;margin-top:12px}

/* partners */
.partners{top:3902px;height:133px;background:linear-gradient(180deg,#d9dadd,#c8cace);display:flex;align-items:center;justify-content:space-between;padding:0 75px}
.badge{background:#f6f6f6;border:2px solid #b6b9c2}
.partner-name{font-family:"Montserrat",Arial,sans-serif;font-weight:700;color:var(--navy)}

/* footer */
.footer{top:4035px;height:366px;text-align:center}
.to-top{width:80px;height:80px;border-radius:50%;border:4px solid var(--orange);margin:100px auto 30px;display:flex;align-items:center;justify-content:center}
.copyright{font-size:13px;color:var(--muted)}
.social{display:flex;justify-content:center;gap:14px;margin-top:20px}
.social i{width:40px;height:40px;border-radius:50%;background:var(--orange);display:block}
.footer-stripe{position:absolute;left:0;bottom:0;width:1200px;height:15px;background:var(--navy)}
</style>
</head>
<body>

<header class="section top-bar">
  <span><svg width="16" height="12" viewBox="0 0 16 12"><rect x="1" y="1" width="14" height="10" fill="none" stroke="#fff" stroke-width="1.5"/><path d="M1 1l7 6 7-6" fill="none" stroke="#fff" stroke-width="1.5"/></svg>info@brakvanbuilders.com</span>
  <span><svg width="14" height="14" viewBox="0 0 24 24"><path d="M6.6 10.8a15.1 15.1 0 006.6 6.6l2.2-2.2a1 1 0 011-.25 11.4 11.4 0 003.6.57 1 1 0 011 1V20a1 1 0 01-1 1A17 17 0 013 4a1 1 0 011-1h3.5a1 1 0 011 1c0 1.25.2 2.45.57 3.57a1 1 0 01-.25 1z" fill="#fff"/></svg>(855) 555-0142</span>
</header>

<section class="section hero">
  <div role="img" aria-label="Smiling contractor in a hard hat and safety vest in front of a city skyline" style="position:absolute;inset:0"></div>
  <nav class="nav">
    <div class="nav-pill"><span class="active">HOME</span><span>ABOUT</span><span>SERVICES</span></div>
    <div class="brand"><i></i>BRAKVAN</div>
    <div class="nav-pill"><span>WORK</span><span>CONTACT</span>
      <svg width="22" height="22" viewBox="0 0 22 22"><circle cx="9" cy="9" r="7" fill="none" stroke="#2b3f8c" stroke-width="3"/><path d="M14 14l6 6" stroke="#2b3f8c" stroke-width="3"/></svg></div>
  </nav>
  <div class="hero-text">
    <h1>BRAKVAN BUILDERS</h1>
    <p>Brakvan Builders takes a Lifetime Relationship approach to solving all our client's construction contracting needs. We believe in leveraging our knowledge with our network to deliver optimal value for our client's properties.</p>
    <span class="btn">CONTACT US</span>
  </div>
  <svg class="hero-arrow" style="left:28px" width="20" height="50" viewBox="0 0 20 50"><path d="M18 2L2 25l16 23" fill="none" stroke="#fff" stroke-width="2"/></svg>
  <svg class="hero-arrow" style="right:28px" width="20" height="50" viewBox="0 0 20 50"><path d="M2 2l16 23L2 48" fill="none" stroke="#fff" stroke-width="2"/></svg>
</section>

<section class="section mission">
  <div class="mission-tag"><span class="heading-mark"></span><h2 class="heading">OUR<br>MISSION</h2></div>
  <div class="mission-copy">
    <p>Brakvan Builders takes a Lifetime Relationship approach to solving all our client's construction contracting needs. We believe in leveraging our knowledge with our network to deliver optimal value for our client's properties. Our team of Experts work hard to ensure that you receive the highest quality craftsmanship and customer service.</p>
    <p>Headquartered in DFW, Brakvan Builders regularly does business with the area's insurance companies, real estate agencies, and property managers. Our extensive relationships with these companies are built on rapid response times and a top quality customer experience.</p>
    <p>Brakvan Builders carries an <span class="rating">"A+" rating with the TSB</span></p>
  </div>
</section>

<section class="section work">
  <div class="work-text">
    <span class="heading-mark"></span>
    <h2 class="heading">OUR <span class="accent">WORK</span></h2>
    <p class="body-copy">It's easy to tell a client what we can do, but we typically let our portfolio and testimonials speak for themselves. Below you will find the most recent projects we completed for very satisfied home owners. It also helps that we have an A rating with the Trade Standards Bureau.</p>
    <p class="body-copy">Please take a moment to view our services and if you have any questions please don't hesitate to call or email us using the form below.</p>
    <span class="btn">CONTACT US</span>
  </div>
  <div class="video">
    <div class="video-frame" role="img" aria-label="Video still of a recent roofing job"></div>
    <span class="video-url">www.brakvanbuilders.com</span>
    <div class="video-badge">BRAKVAN</div>
    <div class="video-bar">
      <svg width="10" height="12" viewBox="0 0 10 12"><path d="M0 0l10 6-10 6z" fill="#ddd"/></svg>
      <span>0:00 / 0:15</span><span class="track"></span>
    </div>
  </div>
</section>

<section class="section services">
  <span class="heading-mark" style="margin-top:40px"></span>
  <h2 class="heading">OUR <span class="accent">SERVICES</span></h2>
  <p class="body-copy services-intro">Brakvan Builders provides professional services for our customers' homes. We work with you to assess your specific needs and guarantee you a custom solution.</p>
  <div class="service-row">
    <div class="service current"><div class="dot"><svg width="40" height="30" viewBox="0 0 40 30"><path d="M3 26L20 6l17 20" fill="none" stroke="#fff" stroke-width="4"/></svg></div><span>ROOFING</span></div>
    <div class="service"><div class="dot"><svg width="36" height="36" viewBox="0 0 36 36"><rect x="4" y="4" width="26" height="10" fill="#fff"/><rect x="16" y="14" width="4" height="18" fill="#fff"/></svg></div><span>PAINTING</span></div>
    <div class="service"><div class="dot"><svg width="36" height="36" viewBox="0 0 36 36"><path d="M4 10h28M4 18h28M4 26h28" stroke="#fff" stroke-width="4"/></svg></div><span>SIDING</span></div>
    <div class="service"><div class="dot"><svg width="36" height="36" viewBox="0 0 36 36"><path d="M4 12v14h28V12" fill="none" stroke="#fff" stroke-width="4"/></svg></div><span>GUTTERS</span></div>
    <div class="service"><div class="dot"><svg width="36" height="36" viewBox="0 0 36 36"><path d="M14 4h8l-2 6 4 20-6 4-6-4 4-20z" fill="#fff"/></svg></div><span>CONSULTING</span></div>
    <div class="service"><div class="dot"><svg width="36" height="36" viewBox="0 0 36 36"><path d="M4 22l14-12 14 6-14 12z" fill="#fff"/></svg></div><span>DRYWALL</span></div>
    <div class="service"><div class="dot"><svg width="36" height="36" viewBox="0 0 36 36"><rect x="6" y="4" width="24" height="28" fill="none" stroke="#fff" stroke-width="3"/><path d="M18 4v28M6 18h24" stroke="#fff" stroke-width="3"/></svg></div><span>WINDOWS</span></div>
    <div class="service"><div class="dot"><svg width="36" height="36" viewBox="0 0 36 36"><path d="M4 10h28M4 18h28M4 26h28M12 10v8M24 18v8" stroke="#fff" stroke-width="3"/></svg></div><span>RETAINING WALL</span></div>
    <div class="service"><div class="dot"><svg width="36" height="36" viewBox="0 0 36 36"><path d="M4 18L18 6l14 12v12H4z" fill="none" stroke="#fff" stroke-width="3"/></svg></div><span>METAL BUILDING</span></div>
    <div class="service"><div class="dot"><svg width="36" height="36" viewBox="0 0 36 36"><path d="M8 8v24M15 6v26M22 6v26M29 8v24M4 14h28M4 26h28" stroke="#fff" stroke-width="3"/></svg></div><span>FENCES</span></div>
  </div>
  <div class="service-panel">
    <span class="panel-notch"></span>
    <div class="art" role="img" aria-label="Illustration of a shingled house roof"></div>
    <h3>ROOFING</h3>
    <p>One of the most important parts of your home is the roof. Your roof protects your home from the elements, helps regulate the inside temperature, and may help lower your energy costs. Gain peace of mind by knowing that your home is covered with a roof that is both aesthetically pleasing and structurally sound. Our complete roof replacements and installations come with our two-year, no-questions-asked emergency response warranty—the best warranty on the market!</p>
  </div>
</section>

<section class="section painting">
  <div class="paint-brands"><span class="b1">Coatline Pro</span><span class="b2">Harrow Paints</span><span class="b3">Ostrel Coatings</span></div>
  <div class="paint-copy">
    <h2>OUR PATINTING SERVICES <span class="accent">HAVE YOU<br>COVERED.</span></h2>
    <p class="sub">Superior Results Require The Best Paints Available.</p>
    <div class="call">Call Us On
      <span class="ring"><svg width="28" height="28" viewBox="0 0 24 24"><path d="M6.6 10.8a15.1 15.1 0 006.6 6.6l2.2-2.2a1 1 0 011-.25 11.4 11.4 0 003.6.57 1 1 0 011 1V20a1 1 0 01-1 1A17 17 0 013 4a1 1 0 011-1h3.5a1 1 0 011 1c0 1.25.2 2.45.57 3.57a1 1 0 01-.25 1z" fill="#fff"/></svg></span>
      (855) 555-0142</div>
  </div>
</section>

<section class="section about">
  <span class="heading-mark" style="margin-top:40px"></span>
  <h2 class="heading">ABOUT <span class="accent">US</span></h2>
  <div class="about-copy body-copy">
    <p>Brakvan Builders takes a customer oriented approach to solving all of our client's needs. Realizing that no two projects are ever the same, Brakvan Builders uses forward thinking techniques to satisfy our customers. While most contracting companies use construction methods that are over half of a century old, Brakvan Builders sets the bar in innovative thinking. With our team of certified adjusters, we work hand in hand with our customers to provide unprecedented customer service and the utmost efficiency.</p>
    <p>Based out of Wise County, Brakvan Builders regularly does business with the area's insurance companies, real estate agencies, and property managers on a regular basis. Our extensive dealings with these company's have resulted in unprecedented response times, and a fast, worry free experience for our customers.</p>
  </div>
  <span class="btn">KNOW MORE</span>
</section>

<section class="section team">
  <span class="heading-mark" style="margin-top:40px"></span>
  <h2 class="heading">ABOUT <span class="accent">US</span></h2>
  <div class="member" style="left:79px">
    <div class="portrait" role="img" aria-label="Portrait of the owner in a hard hat"></div>
    <div class="info"><h4>DORIN BRAKVAN</h4><div class="role">Owner</div>
      <p>With a construction background and marketing degree from Lone Prairie State University as his foundation, Dorin started Brakvan Builders in 2015. Dorin's vision was to develop the most dependable customer service.</p></div>
  </div>
  <div class="member" style="left:600px">
    <div class="portrait" role="img" aria-label="Portrait of the manager"></div>
    <div class="info"><h4>TAVIS BRAKVAN</h4><div class="role">Manager</div>
      <p>Tavis oversees internal operations, account management, and web development for Brakvan Builders.</p></div>
  </div>
</section>

<section class="section contact">
  <span class="heading-mark" style="margin-top:40px;background:var(--navy)"></span>
  <h2 class="heading">CONTACT <span class="accent">US</span></h2>
  <div class="form-title">CONTACT FORM</div>
  <div class="field" style="left:80px;top:205px;width:226px;height:46px">Name*</div>
  <div class="field" style="left:318px;top:205px;width:226px;height:46px">Email*</div>
  <div class="field" style="left:556px;top:205px;width:224px;height:46px">Phone*</div>
  <div class="field" style="left:80px;top:266px;width:700px;height:146px">Message*</div>
  <div class="send"><svg width="40" height="30" viewBox="0 0 40 30"><rect x="2" y="2" width="36" height="26" fill="none" stroke="#fff" stroke-width="3"/><path d="M2 2l18 14L38 2" fill="none" stroke="#fff" stroke-width="3"/></svg></div>
  <div class="info-title">CONTACT INFO</div>
  <div class="info-map" role="img" aria-label="Globe map with a location pin"></div>
  <div class="info-card">
    <strong>BRAKVAN</strong>
    418 Ridgeline Ave. Alder Creek, TX 75010
    <div class="info-line"><svg width="14" height="14" viewBox="0 0 24 24"><path d="M6.6 10.8a15.1 15.1 0 006.6 6.6l2.2-2.2a1 1 0 011-.25 11.4 11.4 0 003.6.57 1 1 0 011 1V20a1 1 0 01-1 1A17 17 0 013 4a1 1 0 011-1h3.5a1 1 0 011 1c0 1.25.2 2.45.57 3.57a1 1 0 01-.25 1z" fill="#f26a21"/></svg>(855) 555-0142</div>
    <div class="info-line"><svg width="14" height="11" viewBox="0 0 16 12"><rect x="1" y="1" width="14" height="10" fill="none" stroke="#f26a21" stroke-width="1.5"/><path d="M1 1l7 6 7-6" fill="none" stroke="#f26a21" stroke-width="1.5"/></svg>info@brakvanbuilders.com</div>
  </div>
</section>

<section class="section partners">
  <div class="badge" style="width:165px;height:62px"></div>
  <div class="badge" style="width:70px;height:70px;border-radius:6px"></div>
  <div class="badge" style="width:80px;height:80px;border-radius:50%"></div>
  <span class="partner-name" style="font-size:22px">Ostrel Coatings</span>
  <div class="badge" style="width:90px;height:66px"></div>
  <span class="partner-name" style="font-size:18px">Harrow Paints</span>
  <span class="partner-name" style="font-size:28px">Coatline Pro</span>
</section>

<footer class="section footer">
  <div class="to-top"><svg width="34" height="20" viewBox="0 0 34 20"><path d="M3 17L17 4l14 13" fill="none" stroke="#f26a21" stroke-width="4"/></svg></div>
  <p class="copyright">© Brakvan Builders - 2017 All rights reserved.</p>
  <div class="social"><i></i><i></i><i></i><i></i></div>
  <div class="footer-stripe"></div>
</footer>

</body>
</html>
```